Website banners + icons

Hello,

For our website www.tolvarmeadow.com who is a very serious website for immigration, integration and naturalisation in Switzerland, we need :

3 x homepage banners : 998px/300px
10 x banners : 998px/150px (concerns the website pages)
icons 24px/24px

The idea is to present a black/white banners with the current text and the theme must be in accordance with the page title.

The graphic line must be very clean and including some fine red informations or line or what ever but very clean and design full.

Please do not use stereotypes like hand shakes...

We are also open to work with abstract things or art.

We let your creativity works on.

Good luck

```html
<!DOCTYPE html>
<html lang="en">
<head>
<meta charset="utf-8">
<title>Tolvar Meadow – Home</title>
<link rel="stylesheet" href="https://fonts.googleapis.com/css2?family=Roboto:wght@300;400;500&display=swap">
<style>
  :root {
    --backdrop-dark: #1f1f1f;
    --backdrop-mid: #3a3a3a;
    --page: #ffffff;
    --ink: #1a1a1a;
    --text-grey: #7a7a7a;
    --heading-grey: #6f6f6f;
    --nav-grey: #666666;
    --accent-red: #d9141b;
    --caption-bg: #2a2a2a;
    --divider: #d4d4d4;
  }
  * { margin: 0; padding: 0; box-sizing: border-box; }
  html, body {
    width: 1200px; height: 770px; overflow: hidden;
  }
  body {
    position: relative;
    background: radial-gradient(ellipse at 50% 40%, var(--backdrop-mid), var(--backdrop-dark) 75%);
    font-family: "Roboto", Arial, sans-serif;
  }
  .page {
    position: absolute; left: 172px; top: 3px;
    width: 877px; height: 767px;
    background: var(--page);
    overflow: hidden;
  }
  .brand {
    position: absolute; left: 21px; top: 82px;
    display: flex; align-items: center; gap: 10px;
    font-size: 25px; font-weight: 400; letter-spacing: 1px;
    color: var(--ink); text-transform: uppercase;
  }
  .brand-mark { width: 14px; height: 14px; background: var(--ink); }
  .language {
    position: absolute; left: 732px; top: 34px;
    display: flex; align-items: center; gap: 7px;
    font-size: 11px; color: #333;
  }
  .language-caret { margin-left: 78px; }
  .main-nav {
    position: absolute; left: 21px; top: 160px;
    display: flex; list-style: none;
    font-size: 10.5px; letter-spacing: 0.8px;
  }
  .main-nav li {
    padding: 0 15px; border-left: 1px solid var(--divider);
    color: var(--nav-grey); line-height: 17px;
  }
  .main-nav li:first-child { padding-left: 0; border-left: 0; }
  .main-nav li.is-active { color: var(--accent-red); }
  .hero {
    position: absolute; left: 0; top: 203px;
    width: 877px; height: 354px;
    background: linear-gradient(90deg, #d6d6d6 0%, #9a9a9a 20%, #3c3c3c 45%, #5a5a5a 70%, #efefef 90%, #f2f2f2 100%);
  }
  .hero-caption {
    position: absolute; left: 431px; top: 203px;
    width: 418px; height: 136px;
    background: var(--caption-bg);
    padding: 4px 0 0 26px;
  }
  .hero-title {
    font-size: 57px; font-weight: 300; color: #fff; line-height: 66px;
    letter-spacing: 0.5px;
  }
  .hero-points { list-style: none; color: var(--accent-red); font-size: 21px; line-height: 26px; font-weight: 300; }
  .section-title {
    position: absolute; left: 21px; top: 596px; width: 835px;
    display: flex; align-items: center; gap: 10px;
    font-size: 17px; letter-spacing: 1px; color: var(--heading-grey); font-weight: 400;
  }
  .section-title::after {
    content: ""; flex: 1; border-top: 2px dotted #cfcfcf; margin-top: 2px;
  }
  .feature { position: absolute; top: 655px; width: 190px; }
  .feature-icon { position: absolute; left: 0; top: 0; }
  .feature-title {
    margin-left: 39px; font-size: 14.5px; font-weight: 400; color: var(--heading-grey); line-height: 22px;
  }
  .feature-text {
    margin: 16px 0 0 39px; width: 146px;
    font-size: 11px; line-height: 16px; color: var(--text-grey); font-weight: 300;
  }
</style>
</head>
<body>
  <div class="page">
    <div class="brand"><span class="brand-mark"></span>Tolvar Meadow</div>

    <div class="language">
      <svg width="17" height="11" viewBox="0 0 17 11" aria-hidden="true">
        <rect width="17" height="11" fill="#1f3a8a"/>
        <path d="M0 0L17 11M17 0L0 11" stroke="#fff" stroke-width="2"/>
        <path d="M8.5 0V11M0 5.5H17" stroke="#fff" stroke-width="3"/>
        <path d="M8.5 0V11M0 5.5H17" stroke="#c8102e" stroke-width="1.6"/>
      </svg>
      <span>English</span>
      <svg class="language-caret" width="8" height="5" viewBox="0 0 8 5" aria-hidden="true"><path d="M0 0H8L4 5Z" fill="#aaa"/></svg>
    </div>

    <ul class="main-nav">
      <li class="is-active">Home</li>
      <li>Services</li>
      <li>Clients</li>
      <li>Blog</li>
      <li>Contact</li>
      <li>About Us</li>
    </ul>

    <div class="hero" role="img" aria-label="Black and white photograph of three colleagues in suits reviewing documents at a laptop"></div>
    <div class="hero-caption" style="top:406px;">
      <h1 class="hero-title">Legal Advice</h1>
      <ul class="hero-points">
        <li>Local legislation</li>
        <li>Contracts</li>
      </ul>
    </div>

    <h2 class="section-title">HOME</h2>

    <div class="feature" style="left:21px;">
      <svg class="feature-icon" width="22" height="22" viewBox="0 0 22 22" aria-hidden="true">
        <rect x="1" y="15" width="3" height="6" fill="var(--accent-red)"/>
        <rect x="6" y="12" width="3" height="9" fill="var(--accent-red)"/>
        <rect x="11" y="8" width="3" height="13" fill="var(--accent-red)"/>
        <rect x="16" y="3" width="3" height="18" fill="var(--accent-red)"/>
      </svg>
      <h3 class="feature-title">Immigration</h3>
      <p class="feature-text">Moving to a new country with different rules and regulations is a big step. Living costs, admini- strative hurdles as well as every day life will be</p>
    </div>

    <div class="feature" style="left:237px;">
      <svg class="feature-icon" width="22" height="22" viewBox="0 0 22 22" aria-hidden="true">
        <path d="M3 19L13 9" stroke="var(--accent-red)" stroke-width="3.5" stroke-linecap="round"/>
        <circle cx="15.5" cy="6.5" r="4.5" fill="var(--accent-red)"/>
        <circle cx="18" cy="4" r="2.3" fill="#fff"/>
        <path d="M4 4L18 18" stroke="var(--accent-red)" stroke-width="3" stroke-linecap="round"/>
      </svg>
      <h3 class="feature-title">Integration</h3>
      <p class="feature-text">After having decided to make Switzerland your home, the conditions of residency will change. Tolvarmeadow offers professional support and</p>
    </div>

    <div class="feature" style="left:453px;">
      <svg class="feature-icon" width="29" height="29" viewBox="0 0 29 29" style="top:-3px;" aria-hidden="true">
        <rect width="29" height="29" fill="var(--accent-red)"/>
        <path d="M11.5 6H17.5V11.5H23V17.5H17.5V23H11.5V17.5H6V11.5H11.5Z" fill="#fff"/>
      </svg>
      <h3 class="feature-title">Naturalization</h3>
      <p class="feature-text">After making Switzerland home, the next step to be considered is obtaining Swiss citizenship. Tolvarmeadow experts safely</p>
    </div>

    <div class="feature" style="left:670px;">
      <svg class="feature-icon" width="28" height="22" viewBox="0 0 28 22" aria-hidden="true">
        <ellipse cx="10" cy="8" rx="9.5" ry="7" fill="var(--accent-red)"/>
        <path d="M4 13L2 19L9 14Z" fill="var(--accent-red)"/>
        <ellipse cx="18.5" cy="11" rx="9" ry="6.5" fill="var(--accent-red)" stroke="#fff" stroke-width="1.5"/>
        <path d="M22 16L26 21L23 15Z" fill="var(--accent-red)"/>
      </svg>
      <h3 class="feature-title">Legal advice</h3>
      <p class="feature-text">Living in a country with a different legal system is a challenge in itself. Tolvarmeadow experts are specialized in contract as</p>
    </div>
  </div>
</body>
</html>
```